2020 Fiber Internet Service Now Available

We want a design a one-sided 8.5x11 FLYER (3 colors) and in PORTRAIT that we can fold ourselves and stuff into a 9-1/2" x 4-1/8" envelope. We want to have a modifiable text box in selected areas of the brochure (with matching font) that we can insert more specialized text/content on an as-needed basis. We would like the delivery of a template we can print from a pdf or Google Docs. The smallest margins possible are appreciated. We do not expect full bleed artwork. If a custom font is used, we want that to be delivered as well so that we can install it on a Windows 10 machine.

The goal of the message is that we are advising the recipient of this flyer that fiber-optic internet service is available at their home or business.

We want possibly some catchy graphics on the brochure. We do not want this to look like 'junk mail'. This needs to be very professional and clean and catchy but not to lose the authenticity of our small, locally-owned business. We are a small fiber optic ISP, competing with the 'big boys' such as Telvora, Brisket and QN&P. We offer the fastest speeds available in these areas that we are investing in. Our plan is to send these to all addresses along a construction route either before or during the construction phase. You can look at our web site at www.klmesh.example. Be sure to click on the Updates menu item as it shows some of our construction projects that we are targeting. It just gives you an idea of what we are accomplishing here in our city. Google reviews and facebook page. https://www.searchly.example/search?q=kl+mesh&oq=kl+mesh https://www.socialpage.example/HollowmereNetworks/

PLEASE NOTE: I ATTACHED HI-RES LOGO GRAPHICS IN THE ZIP FILE. HOWEVER (AND DESPITE THE FACT THAT THE ENVELOPE CURRENTLY HAS IT ON IT) WE ARE MOVING AWAY FROM THE "Wired for you" wording along with removing the green house outline. I attached another png that shows what I'm talking about. The hi-res EPS file should help to allow you to eliminate the unneeded portion of the logo.

As a follow up, we will most likely hire the same designer to do an 3-color envelope design as well that will fit the brochures.

When it comes time for that project, we will be using envelopes that we already had printed with two colors (blue and black). I have attached a photo of the envelope that I took with my phone. Unfortunately, I do not have a design file for this. But, just know that we'll be printing this design on these same envelopes that already have this on it!

Target Market(s)

homes and businesses along a fiber optic construction route

Industry/Entity Type

Internet Service Provider

Requirements
Must have
• For colors, use the colors that are in our logo (attached). one-sided 8.5x11 FLYER (3 colors) and in PORTRAIT
Nice to have
• try not to just copy our web site content.
Should not have
• absolutely no junk mail buzz words. needs to be authentic.

```html
<!DOCTYPE html>
<html lang="en">
<head>
<meta charset="utf-8">
<title>KL Mesh – Fiber Internet Flyer</title>
<link href="https://fonts.googleapis.com/css2?family=Montserrat:wght@500;600;700&family=Questrial&display=swap" rel="stylesheet">
<style>
  :root {
    --page-bg: #e6e6e6;
    --paper: #ffffff;
    --brand-blue: #2f69aa;
    --band-blue: rgba(96, 128, 190, 0.92);
    --panel-dark: #38383a;
    --divider-blue: #2f69aa;
    --ink: #1b1b1b;
    --ink-light: #ffffff;
    --photo-light: #e2e2e2;
    --photo-dark: #6e6e6e;
  }
  * { box-sizing: border-box; margin: 0; padding: 0; }
  html, body { width: 1200px; height: 1080px; overflow: hidden; }
  body {
    background: var(--page-bg);
    font-family: "Questrial", "Helvetica Neue", Arial, sans-serif;
    position: relative;
  }
  .flyer {
    position: absolute;
    left: 210px; top: 35px;
    width: 780px; height: 1010px;
    background: var(--paper);
    box-shadow: 0 8px 30px rgba(0,0,0,0.18);
    padding: 24px;
    display: flex;
    flex-direction: column;
    overflow: hidden;
  }
  .hero {
    position: relative;
    flex: 1 1 auto;
    min-height: 0;
  }
  .hero-photo {
    position: absolute;
    inset: 0;
    background: linear-gradient(120deg, var(--photo-dark) 0%, #9a9a9a 40%, var(--photo-light) 75%, #efefef 100%);
  }
  .logo {
    position: absolute;
    left: 36px; top: 36px;
    width: 270px;
  }
  .logo-bar { height: 22px; background: var(--brand-blue); }
  .logo-box {
    height: 66px;
    background: var(--paper);
    display: flex; align-items: center; justify-content: center; gap: 12px;
  }
  .logo-mark { width: 14px; height: 14px; background: var(--brand-blue); }
  .logo-name {
    font-family: "Montserrat", Arial, sans-serif;
    font-weight: 700;
    font-size: 34px;
    letter-spacing: 2px;
    color: var(--brand-blue);
  }
  .headline-band {
    position: absolute;
    left: 0; right: 0; bottom: 0;
    height: 48px;
    background: var(--band-blue);
    display: flex; align-items: center; justify-content: center;
  }
  .headline {
    font-family: "Montserrat", Arial, sans-serif;
    font-weight: 500;
    font-size: 24px;
    letter-spacing: 3px;
    color: var(--ink-light);
  }
  .intro-panel {
    flex: 0 0 auto;
    background: var(--panel-dark);
    display: flex;
    padding: 16px 26px 18px;
    color: var(--ink-light);
  }
  .intro-column { flex: 1; }
  .intro-divider { width: 3px; background: var(--divider-blue); margin: 4px 22px; }
  .section-title {
    font-family: "Montserrat", Arial, sans-serif;
    font-weight: 500;
    font-size: 22px;
    letter-spacing: 2px;
    margin-bottom: 8px;
  }
  .body-copy {
    font-size: 12px;
    line-height: 1.38;
    letter-spacing: 1.2px;
    text-align: justify;
  }
  .body-copy strong { font-family: "Montserrat", Arial, sans-serif; font-weight: 700; }
  .faq-section {
    flex: 0 0 auto;
    background: var(--brand-blue);
    color: var(--ink-light);
    padding: 24px 34px 26px;
  }
  .faq { width: 440px; }
  .faq-right { margin: 22px 0 0 auto; width: 520px; text-align: right; }
  .faq-title {
    font-family: "Montserrat", Arial, sans-serif;
    font-weight: 500;
    font-size: 22px;
    letter-spacing: 2.5px;
    line-height: 1.25;
    margin-bottom: 10px;
  }
  .faq-right .body-copy { text-align: right; }
  .contact {
    flex: 0 0 auto;
    text-align: center;
    color: var(--ink);
    padding-top: 12px;
  }
  .contact-title {
    font-family: "Montserrat", Arial, sans-serif;
    font-weight: 700;
    font-size: 16px;
    letter-spacing: 2px;
    margin-bottom: 3px;
  }
  .contact-line { font-size: 12px; letter-spacing: 1.4px; line-height: 1.5; }
  .contact-sep { margin: 0 22px; }
</style>
</head>
<body>
  <main class="flyer">
    <div class="hero">
      <div class="hero-photo" role="img" aria-label="Black and white photo of a smiling man in a checked shirt working on a laptop"></div>
      <div class="logo">
        <div class="logo-bar"></div>
        <div class="logo-box">
          <span class="logo-mark"></span>
          <span class="logo-name">KL MESH</span>
        </div>
      </div>
      <div class="headline-band">
        <h1 class="headline">World Class Internet Service for Your Business</h1>
      </div>
    </div>

    <section class="intro-panel">
      <div class="intro-column">
        <h2 class="section-title">About Us</h2>
        <p class="body-copy">After years of trying (and failing) to get the big companies to bring decent internet service to our area, Dana Whitlock decided it was time to solve the problem himself. In 2012, he founded Hollowmere Networks with the goal of offering high speed, unlimited internet service to families in Alderton that had been ignored by other providers. For the first several years, KL offered only fixed wireless internet service.</p>
      </div>
      <div class="intro-divider"></div>
      <div class="intro-column">
        <h2 class="section-title">Why KL Mesh?</h2>
        <p class="body-copy"><strong>KL Mesh is a ‘fiber to the premise’ network.</strong> That means we bring a fiber optic cable all the way to your home or business. This allows us to deliver high speed internet service to you without any potential bottleneck points that could slow things down. No matter what your internet needs might be over the next 10, 20, or 30 years, KL Mesh will keep you online and connected!</p>
      </div>
    </section>

    <section class="faq-section">
      <div class="faq">
        <h2 class="faq-title">Is the service TRULY unlimited?</h2>
        <p class="body-copy">Data limits are brutal. It’s no fun to only be halfway through the month and find out you’ve already maxed out your data allowance! Some internet service providers advertise their service as being ‘unlimited’, but it really isn’t.</p>
      </div>
      <div class="faq faq-right">
        <h2 class="faq-title">How easy will it be to have my questions or concerns addressed?</h2>
        <p class="body-copy">Look to see what other people are saying about the provider’s customer service and the reliability of their internet service. Are questions and concerns addressed quickly and easily, or will you spend an hour on the phone just trying to get a billing question answered?</p>
      </div>
    </section>

    <footer class="contact">
      <h2 class="contact-title">Contact Us</h2>
      <p class="contact-line">We’re happy to discuss our services with you and answer any questions you may have!</p>
      <p class="contact-line">(555) 014-3107<span class="contact-sep">|</span>hello@klmesh.example</p>
    </footer>
  </main>
</body>
</html>
```